Business Card Design

I want a simple and modern design, but also something very catching to the eye.

Also is there anyway that the text can be adjusted or changed so that I may make cards for other employees? If so, please make it so that I may edit the texts at a future date.

Reason: I need all designers to update the business card with my update information.

Industry/Entity Type

Business

Contact Information for Business Card

Owner: Marcus Velliharn
Company Name: Fun Drova
Phone # :555-273-9148
Website: fundrovaplay.com
Email: marc@fundrovaplay.com

```html
<!DOCTYPE html>
<html lang="en">
<head>
<meta charset="utf-8">
<title>Fun Drova – Business Card</title>
<link rel="stylesheet" href="https://fonts.googleapis.com/css2?family=Open+Sans:wght@400;600;700&display=swap">
<style>
  :root {
    --page-bg: #e9e6e1;
    --card-bg: #f6f7f7;
    --card-edge: #dfe3e4;
    --band: #a9d3d6;
    --band-text: #3f6f75;
    --accent-red: #dd2a2a;
    --link-teal: #5ea9af;
    --brand-teal: #1fa3b2;
  }
  * { margin: 0; padding: 0; box-sizing: border-box; }
  html, body {
    width: 1200px;
    height: 1023px;
    overflow: hidden;
    background: var(--page-bg);
    font-family: "Open Sans", Arial, sans-serif;
  }
  .canvas {
    width: 1200px;
    height: 1023px;
    display: flex;
    align-items: center;
    justify-content: center;
  }
  .business-card {
    position: relative;
    width: 520px;
    height: 880px;
    background: var(--card-bg);
    border: 1px solid var(--card-edge);
    box-shadow: 0 10px 30px rgba(0,0,0,0.12);
  }
  .brand {
    position: absolute;
    top: 232px;
    left: 0;
    right: 0;
    display: flex;
    align-items: center;
    justify-content: center;
    gap: 18px;
  }
  .brand-mark {
    width: 52px;
    height: 52px;
    background: var(--brand-teal);
  }
  .brand-name {
    font-size: 56px;
    font-weight: 700;
    color: var(--brand-teal);
    letter-spacing: 1px;
  }
  .name-band {
    position: absolute;
    top: 400px;
    left: 0;
    right: 0;
    height: 98px;
    background: var(--band);
    display: flex;
    align-items: center;
    justify-content: center;
  }
  .person-name {
    font-size: 44px;
    font-weight: 600;
    color: var(--band-text);
    letter-spacing: 1px;
  }
  .person-title {
    position: absolute;
    top: 516px;
    left: 0;
    right: 0;
    text-align: center;
    font-size: 22px;
    font-weight: 600;
    color: var(--accent-red);
    letter-spacing: 0.5px;
  }
  .contact-list {
    position: absolute;
    bottom: 48px;
    left: 0;
    right: 0;
    list-style: none;
    text-align: center;
  }
  .contact-item {
    font-size: 28px;
    font-weight: 400;
    line-height: 1.45;
    color: var(--link-teal);
  }
</style>
</head>
<body>
  <main class="canvas">
    <article class="business-card">
      <div class="brand">
        <span class="brand-mark"></span>
        <span class="brand-name">Fun Drova</span>
      </div>
      <div class="name-band">
        <h1 class="person-name">Marcus Velliharn</h1>
      </div>
      <p class="person-title">Owner - Fun Drova</p>
      <ul class="contact-list">
        <li class="contact-item contact-phone">555-273-9148</li>
        <li class="contact-item contact-web">fundrovaplay.com</li>
        <li class="contact-item contact-email">marc@fundrovaplay.com</li>
      </ul>
    </article>
  </main>
</body>
</html>
```